International non-profit org needs web design

A new non-profit global organization called The Verdant Outreach Collective (VOC) needs a web design. The organization is a global community of professionals engaged in the commercialization aspects of innovation. The members of the community share experience and knowledge about exemplary practices and business models in order to continuoulsy improve the field of expertise.

Target Market(s)

governments, investors, universities, professionala

Industry/Entity Type

Non-Profit

Requirements
Must have
• landing page and capability to add tabs

```html
<!DOCTYPE html>
<html lang="en">
<head>
<meta charset="utf-8">
<title>The Verdant Outreach Collective</title>
<link rel="stylesheet" href="https://fonts.googleapis.com/css2?family=Arimo:wght@400;700&family=Questrial&display=swap">
<style>
:root{
  --red:#d0181f;
  --red-dark:#a90f15;
  --ink:#222;
  --text:#333;
  --muted:#666;
  --panel:#e6e6e6;
  --dark:#2a2320;
  --orange:#e8642a;
  --orange-light:#f29a68;
  --link:#f07a4a;
}
*{box-sizing:border-box;margin:0;padding:0}
html,body{width:1091px;height:1200px;overflow:hidden}
body{background:linear-gradient(#fff,#f6f6f6 60%,#ececec);font-family:Arimo,Arial,sans-serif;color:var(--text)}
.stage{position:relative;width:1000px;height:1100px;transform:scale(1.091);transform-origin:0 0}
.abs{position:absolute}

/* header */
.brand{left:28px;top:44px;display:flex;align-items:center;gap:12px}
.brand-mark{width:26px;height:26px;background:var(--red)}
.brand-name{font-family:Arimo,Arial,sans-serif;font-weight:700;font-size:26px;color:var(--red);line-height:1}
.utility{right:22px;top:32px;font-size:12px;color:#222}
.utility span{margin:0 8px}
.search{left:785px;top:54px;width:193px;height:22px;background:#1b1b1b;color:#ddd;font-size:11px;font-style:italic;padding:5px 10px}
.search svg{position:absolute;right:7px;top:4px}

/* frame */
.frame{left:20px;top:117px;width:958px;height:926px;background:#fff;box-shadow:0 1px 6px rgba(0,0,0,.25)}
.nav{left:20px;top:118px;width:958px;height:37px;display:flex;background:linear-gradient(var(--red),var(--red-dark))}
.nav a{display:flex;align-items:center;justify-content:center;color:#fff;font-weight:700;font-size:15px;text-decoration:none;border-left:1px solid #ef6a6e}
.nav a.active{background:linear-gradient(#555,#2b2b2b);border-left:0}

/* hero */
.hero{left:34px;top:172px;width:932px;height:262px;border-radius:6px;border:2px solid #555;background:linear-gradient(90deg,#8c8f93,#c9cbcd 35%,#dfe1e2 55%,#9ea2a6 80%,#b6b9bc)}
.hero-caption{left:109px;top:174px;width:426px;height:100px;background:rgba(20,20,20,.78);color:#fff;padding:12px 15px}
.hero-caption .lead{font-style:italic;font-weight:700;font-size:22px}
.hero-caption .main{font-weight:700;font-size:31px;margin-top:6px}
.hero-arrow{width:37px;height:37px;background:#222;border:1px solid #777;border-radius:3px;display:flex;align-items:center;justify-content:center}

/* sidebar */
.news{left:35px;top:457px;width:195px;height:291px;background:var(--panel)}
.box-title{font-family:Questrial,sans-serif;font-size:19px;color:#222;padding:7px 8px 6px 35px;border-bottom:1px solid #bbb;margin:0 5px;position:relative}
.box-title i{position:absolute;left:3px;top:9px;width:20px;height:20px;border-radius:50%;background:#fafafa;border:1px solid #999}
.news-item{margin:0 5px;padding:9px 0 7px 20px;border-bottom:1px solid #c6c6c6;font-size:10px;line-height:15px;color:#666;position:relative}
.news-item:before{content:"";position:absolute;left:7px;top:13px;border:3px solid transparent;border-left:4px solid #777}
.news-item:last-child{border:0}
.news-date{margin-bottom:3px}
.letter{left:35px;top:758px;width:195px;height:126px;background:linear-gradient(var(--orange-light),var(--orange));border-radius:2px}
.letter .box-title{color:#fff;border-color:#f6b58f}
.letter .box-title i{background:#f7d25a;border-color:#e8b530;border-radius:2px}
.mail{position:absolute;left:8px;top:52px;width:176px;height:25px;background:#fff;border-radius:6px;font-size:10px;color:#777;padding:6px 17px;border:2px solid #f3c4a8}
.subscribe{position:absolute;left:107px;top:89px;width:75px;height:21px;background:linear-gradient(#ffe04a,#f2b90f);border-radius:4px;font-size:11px;color:#222;text-align:center;line-height:21px}

/* content */
.welcome{left:250px;top:458px;font-family:Questrial,sans-serif;font-weight:400;font-size:22px;color:#222}
.welcome b{color:var(--red);font-family:Arimo,Arial,sans-serif;font-weight:700;font-size:22px}
.intro{left:250px;top:498px;width:710px;font-size:12px;line-height:19.5px;text-align:justify;color:#333}
.btn{background:var(--red);color:#fff;font-size:12px;border-radius:4px;text-align:center;line-height:22px;height:22px}
.card{background:var(--dark);border-radius:4px;color:#ddd}
.card-title{height:44px;background:linear-gradient(#4a403d,var(--dark));border-radius:4px 4px 0 0;font-family:Questrial,sans-serif;font-size:20px;color:#fff;padding:11px 0 0 40px;position:relative}
.card-title i{position:absolute;left:10px;top:13px;width:20px;height:20px;border-radius:50%;background:#f39a1e;display:flex;align-items:center;justify-content:center}
.card p{font-size:11px;line-height:18.5px}
.photo{background:linear-gradient(135deg,#8fb3d6,#dce8f3 50%,#6d8fb4)}
.list{list-style:none;position:absolute;left:25px;top:176px}
.list li{font-size:11px;color:var(--link);text-decoration:underline;height:23px;padding-left:23px;position:relative}
.list li:before{content:"";position:absolute;left:0;top:3px;border:3px solid transparent;border-left:5px solid var(--link)}

/* footer */
.foot{left:34px;top:903px;width:935px;height:128px;background:linear-gradient(#f9f9f9,#ececec);border-radius:3px}
.foot-name{position:absolute;left:16px;top:52px;font-weight:700;font-size:20px;color:#777}
.foot-h{font-family:Questrial,sans-serif;font-size:18px;color:#333}
.foot p,.foot .col{font-size:11px;line-height:18px;color:#333}
.social{display:flex;gap:5px}
.social span{width:26px;height:26px;border-radius:50%;background:#fff;border:1px solid #bbb}
</style>
</head>
<body>
<div class="stage">
  <header>
    <div class="abs brand">
      <div class="brand-mark"></div>
      <div class="brand-name">The Verdant Outreach Collective</div>
    </div>
    <div class="abs utility">HELP<span>|</span>CALL US : 555 - 214 - 3390</div>
    <div class="abs search">Search...
      <svg width="13" height="13" viewBox="0 0 13 13"><circle cx="5" cy="5" r="4" fill="none" stroke="#ddd" stroke-width="1.5"/><line x1="8" y1="8" x2="12" y2="12" stroke="#ddd" stroke-width="1.8"/></svg>
    </div>
  </header>

  <div class="abs frame"></div>
  <nav class="abs nav">
    <a class="active" style="width:112px">Home</a>
    <a style="width:104px">About Us</a>
    <a style="width:90px">Ideas</a>
    <a style="width:135px">Anouncement</a>
    <a style="width:141px">What We Do</a>
    <a style="width:133px">Our Profile</a>
    <a style="width:130px">Contact Us</a>
    <a style="width:113px">Register</a>
  </nav>

  <section>
    <div class="abs hero" role="img" aria-label="Photo of a businessman in a suit looking out an office window over a city"></div>
    <div class="abs hero-caption"><div class="lead">Need Advice for your</div><div class="main">Business Development ?</div></div>
    <div class="abs hero-arrow" style="left:50px;top:290px"><svg width="16" height="16" viewBox="0 0 16 16"><path d="M11 2 5 8l6 6" fill="none" stroke="#fff" stroke-width="3"/></svg></div>
    <div class="abs hero-arrow" style="left:916px;top:290px"><svg width="16" height="16" viewBox="0 0 16 16"><path d="M5 2l6 6-6 6" fill="none" stroke="#fff" stroke-width="3"/></svg></div>
  </section>

  <aside>
    <div class="abs news">
      <div class="box-title"><i></i>Recent News</div>
      <div class="news-item"><div class="news-date">12.10.11</div>Cicero are also reproduced in their exact original form.</div>
      <div class="news-item"><div class="news-date">12.10.11</div>Cicero are also reproduced in their exact original form.</div>
      <div class="news-item"><div class="news-date">12.10.11</div>Cicero are also reproduced in their exact original form.</div>
      <div class="news-item"><div class="news-date">12.10.11</div>Cicero are also reproduced in their exact original form.</div>
    </div>
    <div class="abs letter">
      <div class="box-title"><i></i>News Letter</div>
      <div class="mail">Enter your mail ID</div>
      <div class="subscribe">Subscribe</div>
    </div>
  </aside>

  <main>
    <h1 class="abs welcome">Welcome To <b>VOC</b></h1>
    <p class="abs intro">The standard chunk of Lorem Ipsum used since the 1500s is reproduced below for those interested. Sections 1.10.32 and 1.10.33 from "de Finibus Bonorum et Malorum" by Cicero are also reproduced in their exact original form, accompanied by English versions from the 1914 translation by H. Rackham.</p>
    <div class="abs btn" style="left:872px;top:570px;width:88px">Read more</div>

    <div class="abs card" style="left:249px;top:606px;width:255px;height:278px">
      <div class="card-title"><i><svg width="10" height="10" viewBox="0 0 10 10"><path d="M1 5h7M5 2l3 3-3 3" fill="none" stroke="#fff" stroke-width="2"/></svg></i>What we Do</div>
      <p style="padding:10px 14px 0;text-align:justify">The standard chunk of Lorem Ipsum used since the 1500s is reproduced below for those interested.</p>
      <div class="abs photo" style="left:14px;top:123px;width:227px;height:103px;border-radius:3px" role="img" aria-label="Photo of three colleagues reviewing a document by a large window"></div>
      <div class="abs btn" style="left:153px;top:246px;width:89px">Read more</div>
    </div>

    <div class="abs card" style="left:510px;top:606px;width:449px;height:278px">
      <div class="card-title"><i><svg width="10" height="10" viewBox="0 0 10 10"><path d="M1 5h7M5 2l3 3-3 3" fill="none" stroke="#fff" stroke-width="2"/></svg></i>Who we Are</div>
      <div class="abs" style="left:36px;top:56px;width:72px;height:90px;border-radius:36px 36px 8px 8px;background:radial-gradient(circle at 50% 30%,#9a9a9a,#333 70%)" role="img" aria-label="Illustration of a business person in a suit"></div>
      <p class="abs" style="left:131px;top:54px;width:306px;text-align:justify">The standard chunk of Lorem Ipsum used since the 1500s is reproduced below for those interested. Sections 1.10.32 and 1.10.33 from "de Finibus Bonorum et Malorum" by Cicero are also reproduced in their exact original Rackham.</p>
      <div class="abs btn" style="left:350px;top:136px;width:89px">Read more</div>
      <ul class="list">
        <li>Lorem ipsum dolor sit amet, consectetur adipiscing elit.</li>
        <li>Aliquam volutpat sagittis nisl, nec accumsan dui vestibulum vestibulum.</li>
        <li>Vestibulum aliquam sollicitudin ligula, eleifend lacinia nulla aliquet nec.</li>
        <li>In viverra ultricies lectus, a mattis sem laoreet in.</li>
      </ul>
    </div>
  </main>

  <footer>
    <div class="abs foot">
      <div class="foot-name">VOC</div>
      <div class="abs foot-h" style="left:119px;top:14px">Announcements</div>
      <svg class="abs" style="left:455px;top:20px" width="22" height="10" viewBox="0 0 22 10"><path d="M6 1 1 5l5 4zM16 1l5 4-5 4z" fill="#555"/></svg>
      <div class="abs" style="left:115px;top:43px;width:363px;height:1px;background:#aaa"></div>
      <p class="abs" style="left:118px;top:52px;width:352px;text-align:justify">Lorem Ipsum as their default model text, and a search for 'lorem ipsum' will uncover many web sites still in their infancy. Various versions have evolved over the years.</p>
      <div class="abs" style="left:500px;top:10px;width:1px;height:110px;background:#aaa"></div>
      <div class="abs foot-h" style="left:518px;top:14px">Contact Us</div>
      <div class="abs col" style="left:719px;top:15px">E-Mail &nbsp;: <u>l.hartwell@voc-network.org</u></div>
      <div class="abs col" style="left:518px;top:53px">Dr. Lena Hartwell<br>The Open Markets Roundtable<br>Northbridge Trade Office</div>
      <div class="abs col" style="left:720px;top:53px">id placerat justo.<br>a mauris ornare imperdiet.<br>vel gravida eros.</div>
    </div>
    <div class="abs" style="left:35px;top:1064px;font-size:11px">Copyright © www.voc-network.org All rights reserved</div>
    <div class="abs" style="left:727px;top:1058px;display:flex;align-items:center;gap:6px;font-size:11px">Connect with us :
      <div class="social" aria-label="Social links"><span></span><span></span><span></span><span></span><span></span></div>
    </div>
  </footer>
</div>
</body>
</html>
```